Online tuition webpage design needed

Hi,
We are starting up an online tuition website for non- English speakers wishing to take an QUOLT test.

The webpage must include a place for people to enroll online in the course.
The home page must have:
• room for a logo (coming shortly, blue in colour)
• different packages of online tuition and payvora
• tool bar showing different pages
• perhaps a video, small pictures

This is my site currently:-

www.lingvarotutors.example

as you can see, I am not very sure how to create a website … The large logo is what I would like to use, but I project has not been finalized yet. Please note, I don’t like the logo being that large!

Sites that are similar to what I am doing and like the design of are:

http://www.tesmarilearn.example.au/fees

https://www.brovaskill.example/index.php

http://www.pelgrimtutorkaspar.example.uk/index.html

http://www.quorvanexams.example/

One thing I need is a place for student s to enroll, and if possible, I would like to use quillet to create exercises for students.
Currently, my site is using pagecraftr. My preference is to use quillet for online activities. I am not sure if I can use both.
Thanks in advance

Target Market(s)

people wising to take an QUOLT test (English proficiency test)

Industry/Entity Type

Online

Colors
3276b5
0292cd

Requirements
Must have
• a place for enrollment and admin login for students
quillet
video
talqo, friendwall, chirplo logos
Nice to have
• a booking calender
Should not have
• too much clutter. must be clean and professional looking

```html
<!DOCTYPE html>
<html lang="en">
<head>
<meta charset="utf-8">
<title>QUOLT Online Tuition</title>
<link href="https://fonts.googleapis.com/css2?family=PT+Sans:ital,wght@0,400;0,700;1,400&display=swap" rel="stylesheet">
<style>
:root{
  --brand-blue:#3276b5;
  --sky-blue:#0292cd;
  --band-blue:#3a76b6;
  --card-sky:#1497d5;
  --charcoal:#454545;
  --ink:#3c3c3c;
  --teal:#1fbf8f;
  --white:#ffffff;
  --muted:#555555;
}
*{margin:0;padding:0;box-sizing:border-box}
html,body{width:724px;height:1200px;overflow:hidden;background:var(--white)}
body{font-family:"PT Sans",Arial,sans-serif;color:var(--ink);position:relative}
.abs{position:absolute}

/* header */
.site-header{left:0;top:0;width:724px;height:65px}
.brand{left:72px;top:12px;display:flex;align-items:center;gap:6px}
.brand-mark{width:14px;height:14px;background:var(--brand-blue)}
.brand-name{font-size:23px;font-weight:400;color:var(--brand-blue);line-height:1;letter-spacing:.5px}
.brand-tag{left:108px;top:40px;font-size:8px;color:var(--brand-blue)}
.social{right:262px;top:25px;display:flex;gap:9px;white-space:nowrap}
.social a{display:flex;align-items:center;gap:4px;font-size:9px;line-height:14px;color:var(--sky-blue);text-decoration:none}
.social a span{width:14px;height:14px;background:var(--sky-blue);display:block}
.call{left:481px;top:22px;font-size:12px;line-height:20px;color:var(--muted);display:flex;align-items:center;gap:4px;white-space:nowrap}
.call svg{width:16px;height:20px}
.call .phone{font-size:15px;color:var(--brand-blue);margin-left:2px}

/* hero */
.hero{left:0;top:65px;width:724px;height:322px;overflow:hidden;background:var(--sky-blue)}
.hero-band{left:0;top:252px;width:724px;height:70px;background:var(--band-blue)}
.hero-shine{left:0;top:0}
.hero-photo{left:75px;top:8px;width:270px;height:327px;border-radius:120px 120px 40px 40px;background:linear-gradient(180deg,#2a2a2a 0%,#d9dde2 45%,#3d5f8e 80%,#2d4c78 100%)}
.hero-title{left:418px;top:48px;width:300px;font-size:26px;line-height:37px;color:var(--white);font-weight:400;white-space:nowrap}
.hero-text{left:418px;top:137px;width:245px;font-size:9px;line-height:16px;color:var(--white);white-space:nowrap}
.btn{display:block;text-align:center;color:var(--white);text-decoration:none;font-size:11px;line-height:25px;height:25px}
.btn-enroll{background:var(--teal)}
.btn-detail{background:var(--charcoal)}
.hero .btn{top:275px;width:110px}

/* packages */
.section-title{font-size:20px;font-weight:400;color:var(--ink);letter-spacing:.3px}
.section-title em{font-style:normal;color:var(--brand-blue)}
.packages-title{left:0;top:418px;width:724px;text-align:center}
.card{top:464px;width:185px;height:240px;color:var(--white)}
.card-gold{left:71px;background:var(--charcoal)}
.card-diamond{left:270px;background:var(--card-sky)}
.card-silver{left:468px;background:var(--brand-blue)}
.card-tab{position:absolute;left:30px;top:0;width:126px;height:27px;text-align:center;font-size:14px;line-height:27px}
.card-tab b{font-weight:400;font-size:16px}
.card-gold .card-tab{background:var(--card-sky)}
.card-diamond .card-tab,.card-silver .card-tab{background:var(--charcoal)}
.card h3{position:absolute;left:0;top:44px;width:185px;text-align:center;font-weight:400;font-size:13px}
.features{position:absolute;left:24px;top:75px;list-style:none}
.features li{font-size:9.5px;line-height:25px;padding-left:12px;position:relative;white-space:nowrap}
.features li::before{content:"";position:absolute;left:0;top:9px;border-left:5px solid var(--white);border-top:3.5px solid transparent;border-bottom:3.5px solid transparent}
.card .btn{position:absolute;left:73px;top:203px;width:83px;height:21px;line-height:21px;font-size:9.5px}

/* testimonials */
.students-title{left:72px;top:728px}
.quote-item{left:72px;width:270px;height:45px}
.avatar{position:absolute;left:0;top:0;width:31px;height:31px;border-radius:50%;background:radial-gradient(circle,#c9a58e 0%,#3b2b24 75%)}
.quote-text{position:absolute;left:41px;top:-2px;font-size:9px;line-height:12.5px;font-style:italic;color:var(--muted);white-space:nowrap}
.quote-by{position:absolute;left:42px;top:27px;font-size:9px;color:var(--muted)}
.quote-by a{color:var(--brand-blue);text-decoration:none}

/* video */
.learn-title{left:367px;top:728px}
.video{left:368px;top:770px;width:258px;height:156px;background:linear-gradient(90deg,#6d5a45 0%,#2a221d 45%,#b09d82 100%)}
.video-bar{left:368px;top:912px;width:258px;height:14px;background:rgba(20,20,20,.85)}

/* social quote band */
.tweet-band{left:0;top:961px;width:724px;height:195px;background:var(--band-blue)}
.tweet-badge{left:327px;top:25px;width:70px;height:70px;border-radius:50%;background:var(--white);border:4px solid var(--sky-blue);display:flex;align-items:center;justify-content:center;font-size:11px;color:var(--sky-blue)}
.tweet-text{left:40px;top:103px;width:644px;text-align:center;font-size:16.5px;line-height:22px;color:var(--white)}
.tweet-time{left:0;top:164px;width:724px;text-align:center;font-size:7px;color:var(--white);font-family:Arial,sans-serif}

/* footer */
.site-footer{left:0;top:1156px;width:724px;height:44px;background:var(--teal);color:var(--white);font-family:Arial,sans-serif;font-size:7.5px}
.copyright{left:66px;top:18px}
.legal{right:72px;top:18px}
</style>
</head>
<body>

<header class="site-header abs">
  <div class="brand abs"><span class="brand-mark"></span><span class="brand-name">QUOLT</span></div>
  <div class="brand-tag abs">Online Tuition</div>
  <nav class="social abs">
    <a href="#"><span></span>talqo</a>
    <a href="#"><span></span>friendwall</a>
    <a href="#"><span></span>chirplo</a>
  </nav>
  <div class="call abs">CALL NOW
    <svg viewBox="0 0 16 20"><path d="M4 1 L8 4 L6 7 Q7 11 10 14 L13 12 L16 16 L12 19 Q3 15 1 5 Z" fill="#3276b5"/></svg>
    <span class="phone">0-555-010-482</span>
  </div>
</header>

<section class="hero abs">
  <div class="hero-band abs"></div>
  <svg class="hero-shine abs" width="724" height="322"><polygon points="230,0 300,0 380,322 300,322" fill="#ffffff" opacity=".07"/></svg>
  <div class="hero-photo abs" role="img" aria-label="Photo of a young man sitting cross-legged working on a laptop"></div>
  <h1 class="hero-title abs">Looking for a good<br>QUOLT result first time?</h1>
  <p class="hero-text abs">Lorem <b>ipsum</b> dolor sit amet, consectetur adipiscing elit.<br>Aliquam feugiat et nibh id hendrerit. Sed rhoncus pulvinar<br>ipsum, et <b>commodo nisl</b> sodales vel. Etiam sit amet Duis<br>pellentesque <b>vulputate tortor, ac volutpat</b><br>in. In ultrices metus purus comot es.</p>
  <a class="btn btn-enroll abs" style="left:418px" href="#">ENROLL NOW</a>
  <a class="btn btn-detail abs" style="left:541px" href="#">MORE DETAIL</a>
</section>

<h2 class="section-title packages-title abs">CHOOSE YOUR <em>TUTORIAL PACKAGES</em></h2>

<article class="card card-gold abs">
  <div class="card-tab">GOLD <b>$300</b></div>
  <h3>INCLUDED FEATURES</h3>
  <ul class="features">
    <li>online course for 20 days</li><li>lorem ipusm dolor sit amet</li><li>adipiscing dolor feugiat</li><li>101 practice tests</li><li>lorem ipusm dolor sit amet</li>
  </ul>
  <a class="btn btn-enroll" href="#">ENROLL NOW</a>
</article>
<article class="card card-diamond abs">
  <div class="card-tab">DIAMOND <b>$500</b></div>
  <h3>INCLUDED FEATURES</h3>
  <ul class="features">
    <li>online course for 30 days</li><li>lorem ipusm dolor sit amet</li><li>adipiscing dolor feugiat</li><li>151 practice tests</li><li>lorem ipusm dolor sit amet</li>
  </ul>
  <a class="btn btn-enroll" href="#">ENROLL NOW</a>
</article>
<article class="card card-silver abs">
  <div class="card-tab">SILVER <b>$200</b></div>
  <h3>INCLUDED FEATURES</h3>
  <ul class="features">
    <li>online course for 30 days</li><li>lorem ipusm dolor sit amet</li><li>adipiscing dolor feugiat</li><li>51 practice tests</li><li>lorem ipusm dolor sit amet</li>
  </ul>
  <a class="btn btn-enroll" href="#">ENROLL NOW</a>
</article>

<h2 class="section-title students-title abs">WHAT <em>STUDENTS</em> SAY</h2>
<div class="quote-item abs" style="top:772px">
  <div class="avatar" role="img" aria-label="Student portrait"></div>
  <p class="quote-text">Donec sollicitudin rhoncus porta. Phasellus poret pretium<br>mauris sapien sed arcu. Etiam eu riconvallis.</p>
  <p class="quote-by"><a href="#">Marisol Venn</a> (China)</p>
</div>
<div class="quote-item abs" style="top:821px">
  <div class="avatar" role="img" aria-label="Student portrait"></div>
  <p class="quote-text">Donec sollicitudin rhoncus porta. Phasellus poret pretium<br>mauris sapien sed arcu. Etiam eu riconvallis.</p>
  <p class="quote-by"><a href="#">Marisol Venn</a> (China)</p>
</div>
<div class="quote-item abs" style="top:870px">
  <div class="avatar" role="img" aria-label="Student portrait"></div>
  <p class="quote-text">Donec sollicitudin rhoncus porta. Phasellus poret pretium<br>mauris sapien sed arcu. Etiam eu riconvallis.</p>
  <p class="quote-by"><a href="#">Marisol Venn</a> (China)</p>
</div>

<h2 class="section-title learn-title abs">LEARN <em>MORE</em></h2>
<div class="video abs" role="img" aria-label="Video still of a student with glasses beside a stack of books in a library"></div>
<svg class="video-bar abs" width="258" height="14">
  <polygon points="6,4 6,10 11,7" fill="#ddd"/>
  <rect x="18" y="6" width="180" height="2" fill="#777"/>
  <rect x="18" y="6" width="6" height="2" fill="#ddd"/>
  <rect x="230" y="4" width="7" height="6" fill="none" stroke="#ddd"/>
  <rect x="243" y="4" width="8" height="6" fill="none" stroke="#ddd"/>
</svg>

<section class="tweet-band abs">
  <div class="tweet-badge abs">chirplo</div>
  <p class="tweet-text abs">I highly recommend the QUOLT Online Tuition for people who would like to improve<br>their own score on the QUOLT test and their General English also.</p>
  <p class="tweet-time abs">2 HOURS AGO</p>
</section>

<footer class="site-footer abs">
  <p class="copyright abs">© COPYRIGHT 2014 QUOLT ONLINE TUITION</p>
  <p class="legal abs">PRIVACY &amp; POLICY &nbsp;|&nbsp; TERMS &amp; CONDITIONS</p>
</footer>

</body>
</html>
```